Copperfinch Roofing LLC introduction postcard design

I am looking to get designs for post cards I will be sending out to Homeowners, contractors and Management companies introducing our services, this card will be one sided an area to add a mailing sticker the card will be 4.2x5.5 inches you can get some ideas from www.copperfinchroofing.example

```html
<!DOCTYPE html>
<html lang="en">
<head>
<meta charset="utf-8">
<title>Copperfinch Roofing LLC – Introduction Postcard</title>
<link href="https://fonts.googleapis.com/css2?family=Nunito:ital,wght@0,500;0,700;0,800;1,500;1,600;1,800&display=swap" rel="stylesheet">
<style>
  :root {
    --navy: #26304a;
    --copper: #c8763d;
    --ink: #2f3440;
    --page: #ecebe8;
    --card: #ffffff;
    --wash-a: #e9ecea;
    --wash-b: #d9e0d9;
    --line: #3a3a3a;
  }
  * { box-sizing: border-box; margin: 0; padding: 0; }
  html, body { width: 1200px; height: 800px; overflow: hidden; }
  body { background: var(--page); font-family: "Nunito", sans-serif; color: var(--ink); }

  .postcard {
    position: absolute; left: 50px; top: 20px;
    width: 1100px; height: 760px;
    background: var(--card);
    box-shadow: 0 6px 22px rgba(0,0,0,.18);
    overflow: hidden;
  }
  .postcard__art { position: absolute; inset: 0; }

  .brand {
    position: absolute; left: 34px; top: 60px;
    display: flex; align-items: center; gap: 12px;
    font-weight: 800; font-size: 30px; line-height: 1.05;
    color: var(--navy);
  }
  .brand__dot { width: 34px; height: 34px; border-radius: 50%; background: var(--navy); flex: none; }

  .tagline {
    position: absolute; left: 44px; top: 205px;
    font-style: italic; font-weight: 500; font-size: 19px; line-height: 1.22;
  }
  .section-title {
    position: absolute; left: 48px;
    font-style: italic; font-weight: 800; color: var(--copper);
  }
  .section-title--services { top: 278px; font-size: 25px; }
  .section-title--why { top: 466px; font-size: 19px; left: 55px; }

  .checklist { position: absolute; list-style: none; font-style: italic; font-weight: 600; }
  .checklist li { display: flex; align-items: center; gap: 14px; }
  .checklist svg { width: 18px; height: 18px; flex: none; }
  .checklist--services { left: 50px; top: 314px; font-size: 18px; }
  .checklist--services li { height: 33px; }
  .checklist--why { left: 56px; top: 500px; font-size: 16.5px; }
  .checklist--why li { height: 34px; }

  .contact { position: absolute; left: 62px; top: 626px; list-style: none; font-size: 16.5px; font-weight: 500; }
  .contact li { display: flex; align-items: center; gap: 16px; height: 31px; }
  .contact svg { width: 22px; height: 22px; flex: none; }
</style>
</head>
<body>
<main class="postcard">
  <svg class="postcard__art" width="1100" height="760" viewBox="0 0 1100 760">
    <defs>
      <linearGradient id="wash" x1="0" y1="0" x2="1" y2="1">
        <stop offset="0" stop-color="var(--wash-a)"/>
        <stop offset="1" stop-color="var(--wash-b)"/>
      </linearGradient>
      <radialGradient id="photo-grey" cx=".5" cy=".5" r=".6">
        <stop offset="0" stop-color="#9ba3a8"/><stop offset="1" stop-color="#5f7a4f"/>
      </radialGradient>
      <linearGradient id="photo-red" x1="0" y1="0" x2="0" y2="1">
        <stop offset="0" stop-color="#4d7a45"/><stop offset=".45" stop-color="#5f7d4c"/>
        <stop offset=".55" stop-color="#a54652"/><stop offset="1" stop-color="#8e3440"/>
      </linearGradient>
      <linearGradient id="photo-villa" x1="0" y1="0" x2="0" y2="1">
        <stop offset="0" stop-color="#8fb0c4"/><stop offset=".45" stop-color="#7a6c5e"/>
        <stop offset=".7" stop-color="#e9e2d2"/><stop offset="1" stop-color="#4e7a3e"/>
      </linearGradient>
    </defs>
    <path d="M0 0 H787 L474 760 H0 Z" fill="url(#wash)" role="img" aria-label="Faded aerial view of rooftops in a residential neighbourhood"/>
    <g stroke="var(--navy)" stroke-width="5">
      <circle cx="638" cy="305" r="141" fill="url(#photo-red)" role="img" aria-label="Aerial photo of a red metal roof among trees"/>
      <circle cx="722" cy="140" r="85" fill="url(#photo-grey)" role="img" aria-label="Aerial photo of a grey roof beside a pool"/>
      <circle cx="565" cy="478" r="87" fill="url(#photo-villa)" role="img" aria-label="Photo of a white house with a brown tile roof"/>
    </g>
    <rect x="916" y="220" width="112" height="100" fill="none" stroke="var(--line)" stroke-width="2"/>
    <g stroke="var(--line)" stroke-width="1.5">
      <line x1="727" y1="445" x2="1085" y2="447"/>
      <line x1="731" y1="525" x2="1085" y2="527"/>
      <line x1="735" y1="605" x2="1085" y2="607"/>
    </g>
  </svg>

  <div class="brand"><span class="brand__dot"></span><span>Copperfinch<br>Roofing LLC</span></div>

  <p class="tagline">Your Trusted Roofing Experts<br>in Marlow Shores, Eastport</p>

  <h2 class="section-title section-title--services">Our Roofing Services</h2>
  <ul class="checklist checklist--services">
    <li><svg viewBox="0 0 20 20"><circle cx="10" cy="10" r="8" fill="none" stroke="var(--ink)" stroke-width="2"/><path d="M6 10l3 3 6-7" fill="none" stroke="var(--ink)" stroke-width="2"/></svg>Roof Maintenance Program</li>
    <li><svg viewBox="0 0 20 20"><circle cx="10" cy="10" r="8" fill="none" stroke="var(--ink)" stroke-width="2"/><path d="M6 10l3 3 6-7" fill="none" stroke="var(--ink)" stroke-width="2"/></svg>Roof Repairs</li>
    <li><svg viewBox="0 0 20 20"><circle cx="10" cy="10" r="8" fill="none" stroke="var(--ink)" stroke-width="2"/><path d="M6 10l3 3 6-7" fill="none" stroke="var(--ink)" stroke-width="2"/></svg>Roof Inspection</li>
    <li><svg viewBox="0 0 20 20"><circle cx="10" cy="10" r="8" fill="none" stroke="var(--ink)" stroke-width="2"/><path d="M6 10l3 3 6-7" fill="none" stroke="var(--ink)" stroke-width="2"/></svg>Roof Replacement</li>
  </ul>

  <h2 class="section-title section-title--why">Why Choose Us for Roofing Services?</h2>
  <ul class="checklist checklist--why">
    <li><svg viewBox="0 0 20 20"><circle cx="10" cy="10" r="8" fill="none" stroke="var(--ink)" stroke-width="2"/><path d="M6 10l3 3 6-7" fill="none" stroke="var(--ink)" stroke-width="2"/></svg>Fully Licensed and Insured</li>
    <li><svg viewBox="0 0 20 20"><circle cx="10" cy="10" r="8" fill="none" stroke="var(--ink)" stroke-width="2"/><path d="M6 10l3 3 6-7" fill="none" stroke="var(--ink)" stroke-width="2"/></svg>Experts In Roofing Services</li>
    <li><svg viewBox="0 0 20 20"><circle cx="10" cy="10" r="8" fill="none" stroke="var(--ink)" stroke-width="2"/><path d="M6 10l3 3 6-7" fill="none" stroke="var(--ink)" stroke-width="2"/></svg>Fast, Reliable, and Transparent Services</li>
  </ul>

  <ul class="contact">
    <li><svg viewBox="0 0 22 22"><circle cx="11" cy="11" r="11" fill="var(--navy)"/><path d="M7.5 6.5l2 0 1 2.5-1.3 1a6 6 0 0 0 2.8 2.8l1-1.3 2.5 1v2a1 1 0 0 1-1 1A8.5 8.5 0 0 1 6.5 7.5a1 1 0 0 1 1-1z" fill="#fff"/></svg>(555) 014-2290</li>
    <li><svg viewBox="0 0 22 22"><circle cx="11" cy="11" r="11" fill="var(--navy)"/><rect x="5.5" y="7" width="11" height="8" rx="1" fill="#fff"/><path d="M5.5 7.5l5.5 4 5.5-4" fill="none" stroke="var(--navy)" stroke-width="1.2"/></svg>quick.help@copperfinchroofing.example</li>
    <li><svg viewBox="0 0 22 22"><circle cx="11" cy="11" r="11" fill="var(--navy)"/><g fill="none" stroke="#fff" stroke-width="1.2"><circle cx="11" cy="11" r="6"/><ellipse cx="11" cy="11" rx="2.6" ry="6"/><line x1="5" y1="11" x2="17" y2="11"/></g></svg>www.copperfinchroofing.example</li>
  </ul>
</main>
</body>
</html>
```